KM Group

We need a new website for our company and since we had a very good work done for our logo in this site, we're back for the entire job.

Our company name is Halvorsen Capital Group. We're adding files of examples of what we have done today. In my opinion we need a more attention lock in the site but yet financial simple work.

Our files (attached) will let you know what we have so far. We need a complete change but the colours should be the same, however you can change them not running away to far from the original, and of course matching with the logo.

We need examples for 3 kind of layouts.

- A HOME welcome layout
- An internal Layout with sidebar
- And internal Layout wide

We can buy image licenses if needed for assets.
Actually there are 5 slide images placed on the Welcome HOME, we need those there, but you can improve with better images to match the new website!!!

Target Market(s)

Clients looking for financial advisers, tax and funds specialist, currency advisers

Industry/Entity Type

Financial

Requirements
Must have
• all the fonts must be in accordance with the financial market sites........the welcome home page must be precise, neat and information accurate........the menu should be elegant........main focus on the Home page, should be also the PRIVATE ACCESS box log in.......

```html
<!DOCTYPE html>
<html lang="en">
<head>
<meta charset="utf-8">
<title>Halvorsen Capital Group</title>
<link href="https://fonts.googleapis.com/css2?family=Arimo:wght@400;700&family=Montserrat:wght@400;700&display=swap" rel="stylesheet">
<style>
:root{
  --page:#eee8e2;
  --ink:#2c2c2c;
  --text:#3a3a3a;
  --orange:#f26a1f;
  --orange-dark:#b9461a;
  --panel:#333333;
  --footer:#535353;
  --footer-dark:#383838;
  --green:#1a9a35;
  --red:#d0261f;
  --badge:#cfc8c1;
  --white:#ffffff;
}
*{margin:0;padding:0;box-sizing:border-box}
html,body{width:984px;height:1200px;overflow:hidden}
body{background:var(--page);font-family:"Arimo",Arial,sans-serif;color:var(--text);position:relative}
.topline{position:absolute;left:0;top:0;width:984px;height:3px;background:#2a1e1c}
.sheet{position:absolute;left:212px;top:3px;width:560px;height:768px;background:var(--white);box-shadow:0 0 3px rgba(0,0,0,.12)}
.abs{position:absolute}
/* header */
.brand{left:19px;top:11px;display:flex;align-items:center;gap:6px}
.brand-mark{width:12px;height:12px;background:var(--orange)}
.brand-name{font-family:"Montserrat",sans-serif;font-weight:700;font-size:11px;color:var(--ink);letter-spacing:.3px;line-height:1.2}
.apply{left:450px;top:21px;width:93px;height:24px;background:var(--orange);color:#fff;font-size:7px;font-weight:700;display:flex;align-items:center;justify-content:center;border:1px solid #d9581a}
.nav{left:0;top:68px;width:560px;height:24px;border-top:1px solid #e6e6e6;display:flex;background:linear-gradient(#fff,#f4f4f4)}
.nav a{font-size:6.2px;font-weight:700;color:var(--ink);text-decoration:none;display:flex;align-items:center;justify-content:center;border-right:1px solid #e4e4e4;position:relative}
.nav a.active::after{content:"";position:absolute;left:0;right:0;bottom:0;height:2px;background:var(--orange)}
.nav .caret{color:var(--orange);margin-left:3px;font-size:5px}
/* hero */
.hero{left:0;top:92px;width:560px;height:273px;background:linear-gradient(180deg,#8d98a6 0%,#5c6270 40%,#2c2a2c 75%,#3a2a22 100%)}
.hero-box{left:0;top:80px;width:367px;height:127px;background:rgba(30,30,30,.62)}
.hero-title{left:20px;top:20px;font-family:"Montserrat",sans-serif;font-weight:700;font-size:27px;line-height:27px;color:#fff;letter-spacing:.5px}
.hero-copy{left:19px;top:80px;font-size:10.4px;line-height:14px;color:#fff;width:320px}
.dots{left:19px;top:222px;display:flex;gap:4px}
.dots span{width:18px;height:3px;border:1px solid #fff}
.dots span.on{background:var(--orange);border-color:var(--orange)}
/* ticker */
.ticker{left:0;top:365px;width:560px;height:31px;background:#fff;border-bottom:1px solid #eee;display:flex;align-items:center;font-size:6.4px;font-weight:700;color:var(--ink)}
.ticker .arrow{color:#999;font-size:9px;width:27px;text-align:center}
.rate{margin-right:25px;white-space:nowrap}
.up{color:var(--green)}.down{color:var(--red)}.flat{color:#f39a12}
/* welcome */
.welcome-title{left:18px;top:422px;font-size:17px;font-weight:700;color:#3b3b3b;letter-spacing:-.2px}
.welcome-copy{left:18px;top:447px;width:330px;font-size:8.4px;line-height:12px;color:#222}
.learn{left:17px;top:506px;width:93px;height:25px;background:linear-gradient(#35b9f0,#1291d8);color:#fff;font-size:7px;font-weight:700;display:flex;align-items:center;justify-content:center;border:1px solid #0f84c6}
.access{left:366px;top:422px;width:176px;height:108px;background:var(--panel);border:1px solid #222}
.access-head{height:24px;background:linear-gradient(#d25a21,var(--orange-dark));color:#fff;font-size:9px;font-weight:700;display:flex;align-items:center;padding-left:10px;gap:5px;letter-spacing:.3px}
.field{position:absolute;left:9px;width:157px;height:15px;background:#fff;border:1px solid #999;font-size:5.6px;color:#999;font-weight:700;padding:3px 0 0 9px}
.forgot{position:absolute;left:9px;top:85px;font-size:5.4px;color:#ddd;text-decoration:underline}
.login{position:absolute;left:105px;top:80px;width:61px;height:14px;background:var(--green);color:#fff;font-size:4.4px;font-weight:700;display:flex;align-items:center;justify-content:center}
/* services */
.card{top:560px;width:169px}
.card .pic{height:102px;border:1px solid #ccc}
.card h3{margin-top:12px;text-align:center;color:var(--orange);font-size:10px;font-weight:700}
.card p{margin-top:6px;text-align:center;font-size:7.2px;line-height:10.4px;color:#333}
/* trust */
.verified{left:0;top:788px;width:984px;text-align:center;font-size:7.4px;font-weight:700;color:#333}
.badges{left:337px;top:814px;display:flex;align-items:center;gap:28px}
.badge{height:24px;background:var(--badge);border-radius:2px}
/* footer */
.footer{left:0;top:872px;width:984px;height:173px;background:var(--footer)}
.fcol{position:absolute;top:24px}
.fcol h4{color:var(--orange);font-size:9.2px;font-weight:700;margin-bottom:3px}
.fcol li{list-style:none;font-size:6.4px;line-height:12.6px;color:#eee}
.fcol h4.sub{margin-top:12px}
.bottom{left:0;top:1045px;width:984px;height:155px;background:var(--footer-dark)}
.legal{position:absolute;left:212px;top:22px;width:565px;font-size:6.4px;line-height:12.5px;color:#e6e6e6}
.copy{position:absolute;left:0;top:128px;width:984px;text-align:center;font-size:5.4px;color:var(--orange)}
</style>
</head>
<body>
<div class="topline"></div>

<main class="sheet">
  <div class="abs brand"><span class="brand-mark"></span><span class="brand-name">Halvorsen Capital</span></div>
  <div class="abs apply">APPLY NOW</div>

  <nav class="abs nav">
    <a class="active" style="width:63px">HOME</a>
    <a style="width:72px">ABOUT US<span class="caret">▼</span></a>
    <a style="width:81px">INVESTMENTS<span class="caret">▼</span></a>
    <a style="width:54px">FUNDS<span class="caret">▼</span></a>
    <a style="width:74px">BROKERAGE<span class="caret">▼</span></a>
    <a style="width:70px">EXCHANGE<span class="caret">▼</span></a>
    <a style="width:69px">ACCOUNTS<span class="caret">▼</span></a>
    <a style="width:77px;border-right:none">CONTACT US</a>
  </nav>

  <section class="abs hero" role="img" aria-label="City skyline with lit office towers at dusk beside a river">
    <div class="abs hero-box">
      <h1 class="abs hero-title">Financial<br>Management</h1>
      <p class="abs hero-copy">We offer tailored and flexible solutions for banking and financial management that meets your business's needs.</p>
    </div>
    <div class="abs dots"><span class="on"></span><span></span><span></span><span></span></div>
  </section>

  <div class="abs ticker">
    <span class="arrow">‹</span>
    <span class="rate">GBP / UAH = <span class="up">12.65761 ▲</span></span>
    <span class="rate">GBP / UCX = <span class="down">4010.06174 ▼</span></span>
    <span class="rate">GBP / USD = <span class="up">1.55817 ▲</span></span>
    <span class="rate">GBP / UYU = <span class="up">30.36026 ▲</span></span>
    <span class="rate" style="margin-right:14px">GBP / VEF = <span class="flat">0</span></span>
    <span class="arrow">›</span>
  </div>

  <h2 class="abs welcome-title">Welcome to Halvorsen Capital Group</h2>
  <p class="abs welcome-copy">Lorem ipsum dolor sit amet, consectetuer adipiscing elit, sed diam nonummy nibh euismod tincidunt ut laoreet dolore magna aliquam erat volutpat. Ut wisi enim ad minim veniam, quis nostrud exerci tation ullamcorper suscipit lobortis nisl ut aliquip ex ea commodo.</p>
  <div class="abs learn">LEARN MORE</div>

  <form class="abs access">
    <div class="access-head">
      <svg width="7" height="9" viewBox="0 0 7 9"><rect x="0" y="4" width="7" height="5" fill="#fff"/><path d="M1.5 4V2.5a2 2 0 0 1 4 0V4" stroke="#fff" fill="none"/></svg>
      PRIVATE ACCESS
    </div>
    <div class="field" style="top:32px">Acct. Number</div>
    <div class="field" style="top:55px">Password</div>
    <span class="forgot">Forgot acc number/password?</span>
    <span class="login">LOG IN TO ACCOUNTS</span>
  </form>

  <article class="abs card" style="left:17px">
    <div class="pic" role="img" aria-label="Hand with pen reviewing a printed bar chart and calculator" style="background:linear-gradient(160deg,#f4f4f4,#d9dee2 60%,#9cc24a)"></div>
    <h3>Management &amp; Strategy</h3>
    <p>Lorem ipsum dolor sit amet, consectetuer adipisc ing elit, sed diam nonummy nibh euismod tincidunt ut laoreet dolore magna aliquam erat volutpat. Ut wisi enim ad minim veniam, quis.</p>
  </article>
  <article class="abs card" style="left:196px">
    <div class="pic" role="img" aria-label="Two business people in suits reviewing documents at a desk" style="background:linear-gradient(160deg,#c9d6e6,#5b7396 55%,#1e2c4a)"></div>
    <h3>Funds</h3>
    <p>Lorem ipsum dolor sit amet, consectetuer adipisc ing elit, sed diam nonummy nibh euismod tincidunt ut laoreet dolore magna aliquam erat volutpat. Ut wisi enim ad minim veniam, quis.</p>
  </article>
  <article class="abs card" style="left:374px">
    <div class="pic" role="img" aria-label="Golden dollar signs over a currency chart" style="background:linear-gradient(150deg,#7a4e12,#d99a2a 45%,#f5d47a 70%,#a86a18)"></div>
    <h3>Currency Exchange</h3>
    <p>Lorem ipsum dolor sit amet, consectetuer adipisc ing elit, sed diam nonummy nibh euismod tincidunt ut laoreet dolore magna aliquam erat volutpat. Ut wisi enim ad minim veniam, quis.</p>
  </article>
</main>

<p class="abs verified">Verified and Protected by</p>
<div class="abs badges" role="img" aria-label="Certification badges">
  <span class="badge" style="width:60px"></span>
  <span class="badge" style="width:76px"></span>
  <span class="badge" style="width:50px"></span>
  <span class="badge" style="width:68px"></span>
</div>

<footer class="abs footer">
  <div class="fcol" style="left:212px"><h4>About Us</h4><ul><li>History</li><li>Expertize</li><li>Identity</li><li>Strategy</li><li>Contact Us</li></ul></div>
  <div class="fcol" style="left:301px"><h4>Investments</h4><ul><li>Term Deposits</li><li>Management &amp; Strategy</li><li>Client Relations</li><li>Financial Privacy</li><li>Tax Advice</li><li>Wealth Analysis &amp; Financial Planning</li><li>Active Advisory Group</li><li>Manager Selection Services</li><li>Private Equity</li></ul></div>
  <div class="fcol" style="left:462px"><h4>Investments</h4><ul><li>Overview</li><li>Administration</li><li>Funds Security</li><li>Core Security</li><li>Reporting</li><li>Revenue Opportunities</li><li>How It Works?</li><li>Glossary</li></ul></div>
  <div class="fcol" style="left:579px"><h4>Currency Exchange</h4><ul><li>Foreign Exchange</li><li>Fx Forward</li><li>Fx Options</li></ul><h4 class="sub">Accounts</h4><ul><li>Apply Now</li><li>Private Access</li></ul></div>
  <div class="fcol" style="left:716px"><h4>Brokerage</h4><ul><li>Foreign Exchange</li><li>Fx Forward</li><li>Fx Options</li></ul></div>
</footer>

<section class="abs bottom">
  <p class="legal">Lorem ipsum dolor sit amet, consectetuer adipiscing elit, sed diam nonummy nibh euismod tincidunt ut laoreet dolore magna aliquam erat volutpat. Ut wisi enim ad minim veniam, quis nostrud exerci tation ullamcorper suscipit lobortis nisl ut aliquip ex ea commodo consequat. Duis autem vel eum iriure dolor in hendrerit in vulputate velit esse molestie conse quat, vel illum dolore eu feugiat nulla facilisis at vero eros et accumsan et iusto odio dignissim qui blandit praesent luptatum zzril delenit augue duis dolore te feugait nulla facilisi. Epsum factorial non deposit quid pro quo hic escorol. Olypian quarrels et gorilla congolium sic ad nauseum. Souvlaki ignitus carborundum e pluribus unum. Defacto lingo est igpay atinlay. Marquee selectus non provisio incongruous feline nolo contendre. Gratuitous octopus niacin, sodium glutimate. Quote meon an estimate et non interruptus stadium. Sic tempus fugit esperanto hiccup estrogen. Glorious baklava ex librus hup hey ad infinitum. Non sequitur condominium facile et geranium incognito.</p>
  <p class="copy">COPYRIGHT © 2013 HALVORSEN CAPITAL GROUP. ALL RIGHTS RESERVED.</p>
</section>
</body>
</html>
```